Capability Statement Document/Flyer

Take the existing words from the capability statement document (attached) and design a unique folder/flyer document for professional use. Maybe something like a trifold or bifold style. Use approved colours and logo as per the attached files.
Our company designs and builds small onshore gas processing plants.

```html
<!DOCTYPE html>
<html lang="en">
<head>
<meta charset="utf-8">
<title>Veridan Capability Statement 2026</title>
<link href="https://fonts.googleapis.com/css2?family=Poppins:wght@400;500;600;700&display=swap" rel="stylesheet">
<style>
:root{
  --teal:#177a6a;
  --teal-dark:#116557;
  --teal-soft:#d9ece8;
  --teal-photo:#5fbcaa;
  --ink:#161616;
  --grey:#ebebeb;
  --grey-line:#cfcfcf;
  --paper:#ffffff;
  --orange:#fdb56b;
  --orange-deep:#dc9450;
}
*{box-sizing:border-box;margin:0;padding:0}
html,body{width:1200px;height:2530px;overflow:hidden}
body{font-family:"Poppins",sans-serif;color:var(--ink);background:var(--orange)}
.stage{position:relative;width:1222px;height:2576px;transform:scale(0.98200);transform-origin:0 0;
  background:
    radial-gradient(ellipse 560px 360px at 585px 995px,var(--orange-deep) 0,rgba(220,148,80,0) 100%),
    radial-gradient(ellipse 560px 360px at 585px 1610px,var(--orange-deep) 0,rgba(220,148,80,0) 100%),
    radial-gradient(ellipse 300px 340px at 611px 370px,#eea45c 0,rgba(238,164,92,0) 100%),
    radial-gradient(ellipse 300px 340px at 585px 2230px,#eea45c 0,rgba(238,164,92,0) 100%),
    var(--orange);}
.page{position:absolute;width:402px;height:520px;background:var(--paper);overflow:hidden}
.spread{position:absolute;left:183px;width:804px;height:520px;box-shadow:0 10px 40px rgba(140,70,10,.25)}
.spread .page{top:0}
.spread .page.left{left:0}
.spread .page.right{left:402px}
.spread .fold{position:absolute;left:372px;top:0;width:60px;height:520px;
  background:linear-gradient(90deg,rgba(0,0,0,0) 0,rgba(0,0,0,.05) 45%,rgba(0,0,0,.08) 50%,rgba(0,0,0,.03) 55%,rgba(0,0,0,0) 100%);pointer-events:none}
.abs{position:absolute}
.teal{color:var(--teal)}
/* brand */
.brand{position:absolute;display:flex;align-items:center;gap:6px;font-weight:600;color:var(--teal);letter-spacing:.02em}
.brand .mark{display:block;border:0;background:var(--teal)}
/* cover */
.cover{left:410px;top:103px;box-shadow:0 10px 40px rgba(140,70,10,.22)}
.back{left:384px;top:1965px;box-shadow:0 10px 40px rgba(140,70,10,.22)}
.big-title{position:absolute;font-weight:600;line-height:1;letter-spacing:-.01em}
.big-title span{display:block}
.big-title .second{color:var(--teal)}
.year{position:absolute;font-weight:600;color:var(--grey);line-height:1;transform-origin:0 0;transform:rotate(-90deg);white-space:nowrap}
.tagline-box{position:absolute;background:var(--teal);color:#fff;font-weight:400;line-height:1.2}
.photo{position:absolute}
.url{position:absolute;font-size:6px;font-weight:600;color:var(--teal)}
/* inner pages */
.run-head{position:absolute;left:37px;top:30px;display:flex;align-items:center;gap:6px}
.run-head .doc{font-size:7px;font-weight:700;line-height:1}
.run-head .doc span{display:block;color:var(--teal)}
.run-head .sep{width:1px;height:14px;background:var(--ink)}
.run-head .tag{font-size:5px;font-weight:500}
.corner-arc{position:absolute;left:0;top:0}
.foot{position:absolute;left:37px;right:56px;top:503px;display:flex;align-items:center;gap:10px;font-size:5px;font-weight:600}
.right .foot{left:56px;right:37px}
.foot .rule{flex:1;height:1px;background:linear-gradient(90deg,var(--grey-line),var(--grey-line) 20%,transparent 20%,transparent 22%,var(--grey-line) 22%,var(--grey-line) 78%,transparent 78%,transparent 80%,var(--grey-line) 80%)}
.foot .web{color:var(--teal)}
.h-section{position:absolute;font-size:8px;font-weight:600;color:var(--teal)}
.body-copy{position:absolute;font-size:5.4px;line-height:1.45}
.page-title{position:absolute;left:37px;top:80px;font-size:22px;font-weight:500}
.page-title span{color:var(--teal)}
.black-bar{position:absolute;left:37px;top:143px;width:309px;height:18px;background:var(--ink);color:#fff;font-size:7.6px;padding:0 6px;line-height:18px}
.principle{position:absolute;left:37px;width:309px;height:20px;display:flex;gap:4px}
.principle .num{width:18px;height:20px;background:var(--teal);color:#fff;font-size:7px;display:flex;align-items:center;justify-content:center}
.principle .txt{flex:1;border:1px solid var(--teal);color:var(--teal);font-size:6.2px;display:flex;align-items:center;padding-left:6px}
.org{position:absolute;left:37px;top:340px;width:309px;height:97px;background:#efefef;border-radius:3px}
.org .row{position:absolute;left:8px;right:10px;height:20px;display:flex;gap:5px}
.org .lbl{width:94px;background:#fff;color:var(--teal);font-size:5.4px;display:flex;align-items:center;padding-left:4px}
.org .cell{flex:1;background:var(--teal);color:#fff;font-size:5.4px;display:flex;align-items:center;padding-left:4px}
/* tables */
.grid-table{position:absolute;border-collapse:collapse;table-layout:fixed}
.grid-table th{background:var(--teal);color:#fff;font-size:7px;font-weight:600;text-align:left;padding:0 4px;border-right:1px solid #fff}
.grid-table td{font-size:7px;line-height:1.15;padding:0 4px;border-bottom:1px solid var(--grey-line);border-right:1px solid var(--grey-line);vertical-align:middle}
.grid-table td:last-child,.grid-table th:last-child{border-right:0}
.grid-table td.fn{font-weight:600}
.grid-table td.idx{text-align:center;color:var(--teal);font-size:6.4px}
.services{left:56px;top:93px;width:309px}
.services thead tr{height:26px}
.services tbody tr{height:29.5px}
.services tbody tr:last-child td{border-bottom:2px solid var(--teal)}
.roles{left:37px;top:94px;width:309px}
.roles thead tr{height:24px}
.roles tbody tr{height:26.4px}
.roles td{border-right:0}
.roles tbody tr:last-child td{border-bottom:2px solid var(--teal)}
.list-box{position:absolute;left:37px;width:309px;border:1px solid var(--grey-line);border-bottom:4px solid var(--teal);border-radius:2px;padding:7px 8px}
.list-box li{list-style:none;font-size:5.6px;font-weight:500;line-height:10.2px;padding-left:9px;position:relative}
.list-box li::before{content:"";position:absolute;left:1px;top:3.4px;width:3px;height:3px;border-right:1px solid var(--ink);border-top:1px solid var(--ink);transform:rotate(45deg)}
.contact-line{position:absolute;left:37px;top:468px;font-size:5.6px;font-weight:500}
.contact-line span{color:var(--teal)}
/* personnel */
.person{position:absolute;left:56px;width:309px}
.person .head{display:grid;grid-template-columns:80px 69px 58px 102px;height:19px;background:var(--teal);color:#fff;font-size:7px;font-weight:600}
.person .head div{display:flex;align-items:center;padding-left:4px;border-right:1px solid #fff}
.person .head div:last-child{border-right:0}
.person .exp{display:grid;grid-template-columns:80px 229px;background:var(--teal-soft);font-size:5.4px;min-height:17px}
.person .exp div{display:flex;align-items:center;padding:2px 4px;line-height:1.3}
.person .exp div:first-child{font-weight:600}
.person p{font-size:5.4px;line-height:1.4;padding:6px 4px 0}
.person .rule{margin-top:8px;height:1px;background:var(--grey-line)}
/* back contact */
.contact-title{position:absolute;left:53px;top:466px;font-size:8px;font-weight:600;color:var(--teal)}
.contact-rule{position:absolute;left:53px;right:36px;top:481px;height:1px;background:var(--grey-line)}
.contact-item{position:absolute;top:487px;display:flex;gap:4px;font-size:4.8px;line-height:1.5}
.contact-item svg{flex:none}
</style>
</head>
<body>
<div class="stage">

  <!-- Front cover -->
  <section class="page cover">
    <div class="brand" style="left:250px;top:36px;font-size:25px"><span class="mark" style="width:10px;height:10px"></span>VERIDAN</div>
    <div class="year" style="left:334px;top:520px;font-size:112px">2026</div>
    <h1 class="big-title" style="left:38px;top:160px;font-size:37px"><span>CAPABILITY</span><span class="second">STATEMENT</span></h1>
    <div class="abs" style="left:0;top:245px;width:320px;height:12px;background:var(--grey)"></div>
    <div class="tagline-box" style="left:38px;top:257px;width:281px;height:52px;padding:12px 10px;font-size:12px">Simplify Project Execution,<br>Streamline Operations</div>
    <div class="photo" role="img" aria-label="Photo of a gas processing plant between rows of solar panels under a blue sky" style="left:0;top:309px;width:319px;height:153px;background:linear-gradient(180deg,#4f6fa0 0%,#8ca8cc 45%,#c9d3d8 62%,#b9a78d 78%,#8b7a63 100%)"></div>
    <div class="url" style="left:38px;top:472px">www.veridan.com.au</div>
  </section>

  <!-- Spread: pages 02–03 -->
  <section class="spread" style="top:735px">
    <div class="page left">
      <svg class="corner-arc" width="90" height="60" viewBox="0 0 90 60" aria-hidden="true"><path d="M-4 48 Q20 6 82 -4" fill="none" stroke="var(--grey)" stroke-width="16"/></svg>
      <div class="run-head"><div class="doc">CAPABILITY<span>STATEMENT</span></div><div class="sep"></div><div class="tag">Simplify Project Execution, Streamline Operations</div></div>
      <h2 class="page-title">Who are <span>Veridan?</span></h2>
      <p class="body-copy" style="left:37px;top:110px;width:309px">Veridan are a highly experienced team of Executive, Project, Construction, Commissioning and Operations specialists who combine deep technical knowledge with proven leadership to deliver unique Project Delivery Partner services to organisations in Australia.</p>
      <div class="black-bar">Simplify Project Execution, Streamline Operations.</div>
      <h3 class="h-section" style="left:37px;top:184px">What is a Project Delivery Partner?</h3>
      <p class="body-copy" style="left:37px;top:199px;width:309px">A Project Delivery Partner (PDP) provides integrated project management along with technical, commercial and delivery support services to help an organisation successfully deliver a project. The PDP acts as the owner's team while the owner retains accountability and key decision-making authority.</p>
      <h3 class="h-section" style="left:37px;top:248px">PDP Core Principles:</h3>
      <div class="principle" style="top:263px"><div class="num">1</div><div class="txt">Owner controls the project</div></div>
      <div class="principle" style="top:286px"><div class="num">2</div><div class="txt">PDP enables delivery &amp; provides assurance</div></div>
      <div class="principle" style="top:310px"><div class="num">3</div><div class="txt">Contractors execute the work</div></div>
      <div class="org">
        <div class="row" style="top:9px"><div class="lbl">Owner</div><div class="cell">Operator XYZ</div></div>
        <div class="row" style="top:40px"><div class="lbl">Project Delivery Partner</div><div class="cell">Veridan</div></div>
        <div class="row" style="top:70px"><div class="lbl">Contractors</div><div class="cell">Engineering</div><div class="cell">Engineering</div><div class="cell">Execution</div></div>
      </div>
      <h3 class="h-section" style="left:37px;top:447px">PDP Objective:</h3>
      <p class="body-copy" style="left:37px;top:459px;width:309px">Deliver the project safely, on schedule, within budget and ready for operations; providing owner capability throughout the project lifecycle.</p>
      <div class="foot"><span>02</span><span class="rule"></span><span class="web">www.veridan.com.au</span></div>
    </div>
    <div class="page right">
      <div class="brand" style="left:292px;top:25px;font-size:14px"><span class="mark" style="width:6px;height:6px"></span>VERIDAN</div>
      <h3 class="h-section" style="left:56px;top:76px">PDP Services:</h3>
      <table class="grid-table services">
        <colgroup><col style="width:24px"><col style="width:85px"><col style="width:200px"></colgroup>
        <thead><tr><th style="text-align:center">#</th><th>Function</th><th>Veridan Service</th></tr></thead>
        <tbody>
          <tr><td class="idx">1</td><td class="fn">Project Management</td><td>Planning, Reporting &amp; Delivery Leadership from Concept to Completion</td></tr>
          <tr><td class="idx">2</td><td class="fn">Engineering</td><td>Concept Selection, Design Coordination, Technical Assurance &amp; Value Engineering</td></tr>
          <tr><td class="idx">3</td><td class="fn">Procurement</td><td>Contracting Strategy, Tender Process &amp; Supplier/Contractor Management</td></tr>
          <tr><td class="idx">4</td><td class="fn">Approvals</td><td>Land Access, Regulator Engagement, Safety Case, Permits &amp; Licenses</td></tr>
          <tr><td class="idx">5</td><td class="fn">Cost Control</td><td>Budget Development, Forecasting &amp; Management</td></tr>
          <tr><td class="idx">6</td><td class="fn">Scheduling</td><td>Master Schedule Development, WBS, Resource Allocation, Monitoring &amp; Updating</td></tr>
          <tr><td class="idx">7</td><td class="fn">Risk Management</td><td>Risk Register, Identification, Mitigation &amp; Reporting</td></tr>
          <tr><td class="idx">8</td><td class="fn">Governance</td><td>Framework, Stage Gates, Change control, Reporting &amp; Decision Support</td></tr>
          <tr><td class="idx">9</td><td class="fn">Construction</td><td>Management &amp; Coordination of Contractor Execution Teams</td></tr>
          <tr><td class="idx">10</td><td class="fn">Commissioning &amp; Start-up</td><td>Lead Commissioning &amp; Start-up, Completions System, Bring the Facility to Steady-State</td></tr>
          <tr><td class="idx">11</td><td class="fn">Operations Readiness</td><td>People &amp; Organisation, Process &amp; Procedures, Systems &amp; Technology</td></tr>
          <tr><td class="idx">12</td><td class="fn">Operations &amp; Maintenance</td><td>Monitor &amp; Operate Asset, Minimize Downtime, Lowest Possible OPEX for Owner</td></tr>
        </tbody>
      </table>
      <div class="foot"><span class="web">www.veridan.com.au</span><span class="rule"></span><span>03</span></div>
    </div>
    <div class="fold"></div>
  </section>

  <!-- Spread: pages 04–05 -->
  <section class="spread" style="top:1350px">
    <div class="page left">
      <svg class="corner-arc" width="90" height="60" viewBox="0 0 90 60" aria-hidden="true"><path d="M-4 48 Q20 6 82 -4" fill="none" stroke="var(--grey)" stroke-width="16"/></svg>
      <div class="run-head"><div class="doc">CAPABILITY<span>STATEMENT</span></div><div class="sep"></div><div class="tag">Simplify Project Execution, Streamline Operations</div></div>
      <h3 class="h-section" style="left:37px;top:76px">PDP Roles &amp; Responsibilities:</h3>
      <table class="grid-table roles">
        <colgroup><col style="width:73px"><col style="width:236px"></colgroup>
        <thead><tr><th>Owner</th><th>Veridan Service</th></tr></thead>
        <tbody>
          <tr><td class="fn">Sets Project Objectives</td><td>Develops Delivery Plans</td></tr>
          <tr><td class="fn">Approves Major Decisions</td><td>Provides Recommendations</td></tr>
          <tr><td class="fn">Holds Project Risk</td><td>Identifies and Manages Risks</td></tr>
          <tr><td class="fn">Awards Contracts</td><td>Manages Contractor Interfaces</td></tr>
          <tr><td class="fn">Provides Funding</td><td>Monitors Cost and Schedule Performance</td></tr>
        </tbody>
      </table>
      <h3 class="h-section" style="left:37px;top:272px">PDP Benefits:</h3>
      <ul class="list-box" style="top:287px;height:69px">
        <li>Provides owners with access to experienced project delivery capability</li>
        <li>Improved project controls and governance</li>
        <li>Greater flexibility than traditional EPC delivery</li>
        <li>Enhanced visibility and management of cost, schedule and risk</li>
        <li>Scalable resources aligned with project phases</li>
      </ul>
      <h3 class="h-section" style="left:37px;top:373px">PDP Challenges:</h3>
      <ul class="list-box" style="top:389px;height:59px">
        <li>Owner retains significant delivery risk</li>
        <li>Requires clear governance and decision-making processes</li>
        <li>Multiple contractor interfaces require strong coordination</li>
        <li>Success depends on collaborative Owner-PDP relationship</li>
      </ul>
      <p class="contact-line">For More Information Contact: <span>directors@veridan.com.au</span></p>
      <div class="foot"><span>04</span><span class="rule"></span><span class="web">www.veridan.com.au</span></div>
    </div>
    <div class="page right">
      <div class="brand" style="left:286px;top:25px;font-size:17px"><span class="mark" style="width:7px;height:7px"></span>VERIDAN</div>
      <h3 class="h-section" style="left:56px;top:76px">Key Veridan Personnel</h3>

      <div class="person" style="top:94px">
        <div class="head"><div>Owner</div><div>Martin Hale</div><div>Role:</div><div>Executive Director</div></div>
        <div class="exp"><div>35yrs Exp:</div><div>Corvex, Northwind Energy, Halden, Ardent Gas</div></div>
        <p>Extensive global energy industry experience, from frontline O&amp;M to the boardroom. Respected 'C Suite' leader with a track record of building high performing teams that deliver outstanding results.</p>
        <div class="rule"></div>
      </div>

      <div class="person" style="top:190px">
        <div class="head"><div>Name:</div><div>Alistair Reid</div><div>Role:</div><div>Technical Director</div></div>
        <div class="exp" style="min-height:26px"><div>39yrs Exp:</div><div>Corvex, Northwind Energy, Gulf Basin Petroleum, Meridian, Coastal Group, Bayline Gas, Halden, Ardent Gas</div></div>
        <p>Highly skilled &amp; experienced operations &amp; project management professional with 39 years' experience in the global oil &amp; gas industry delivering multiple projects and establishing best in class operational assets. Deep knowledge of project management, construction, commissioning &amp; start-up including a global functional assurance role.</p>
        <div class="rule"></div>
      </div>

      <div class="person" style="top:300px">
        <div class="head"><div>Name:</div><div>Graham Tully</div><div>Role:</div><div>Commercial Director</div></div>
        <div class="exp"><div>40yrs Exp:</div><div>Redcliff, Kestrel, Meridian, Halden, Ardent Gas</div></div>
        <p>Senior Logistics &amp; Supply Chain Manager / Procurement Manager with strong operational, commercial, project management, negotiating &amp; relationship building skills. Experienced in operating complex and diverse logistics operations, significantly improving service levels whilst reducing cost.</p>
        <div class="rule"></div>
      </div>

      <div class="person" style="top:395px">
        <div class="head"><div>Name:</div><div>Ewan Barclay</div><div>Role:</div><div>Operations Director</div></div>
        <div class="exp"><div>27yrs Exp:</div><div>Meridian, Coastal Group, Bayline Gas, Halden, Ardent Gas</div></div>
        <p>27 years' success leading operations, maintenance and commissioning teams on onshore and offshore oil and gas production platforms, FPSOs, gas processing, coal seam gas, refrigeration facilities, and chemical refineries. Results driven and enthusiastic Leader with a proven track record of delivery.</p>
      </div>

      <div class="foot"><span class="web">www.veridan.com.au</span><span class="rule"></span><span>05</span></div>
    </div>
    <div class="fold"></div>
  </section>

  <!-- Back cover -->
  <section class="page back">
    <div class="year" style="left:306px;top:455px;font-size:104px">2026</div>
    <div class="abs" style="left:53px;top:243px;width:349px;height:12px;background:var(--grey)"></div>
    <h1 class="big-title" style="left:127px;top:184px;font-size:29px"><span>CAPABILITY</span><span class="second">STATEMENT</span></h1>
    <div class="photo" role="img" aria-label="Teal-tinted photo of gas processing plant pipework and vessels" style="left:53px;top:255px;width:349px;height:205px;background:linear-gradient(180deg,#a9dcd2 0%,#72c3b3 35%,#3f9f8c 70%,#2b7d6d 100%)"></div>
    <div class="tagline-box" style="left:127px;top:255px;width:275px;height:40px;padding:9px 8px;font-size:10px;background:var(--teal)">Simplify Project Execution,<br>Streamline Operations</div>
    <h3 class="contact-title">Contact Us</h3>
    <div class="contact-rule"></div>
    <div class="contact-item" style="left:53px">
      <svg width="7" height="9" viewBox="0 0 7 9" aria-hidden="true"><path d="M3.5 0C1.6 0 0 1.5 0 3.4 0 5.9 3.5 9 3.5 9S7 5.9 7 3.4C7 1.5 5.4 0 3.5 0Z" fill="var(--teal)"/><circle cx="3.5" cy="3.4" r="1.3" fill="#fff"/></svg>
      <div>48 Harbour St Ste 12<br>Port City 0000</div>
    </div>
    <div class="contact-item" style="left:138px">
      <div style="display:flex;flex-direction:column;gap:2px">
        <svg width="7" height="7" viewBox="0 0 7 7" aria-hidden="true"><circle cx="3.5" cy="3.5" r="3.5" fill="var(--teal)"/><path d="M2.2 1.8l.8 1-.4.5c.3.6.7 1 1.3 1.3l.5-.4 1 .8-.5.8C3.3 5.5 1.5 3.7 1.3 2.2Z" fill="#fff"/></svg>
        <svg width="7" height="6" viewBox="0 0 7 6" aria-hidden="true"><rect width="7" height="6" fill="var(--teal)"/><path d="M0 0l3.5 3L7 0" fill="none" stroke="#fff" stroke-width=".7"/></svg>
      </div>
      <div>+61 000.0000.0000<br>info@veridan.com.au</div>
    </div>
    <div class="url" style="left:298px;top:491px;font-size:5px">www.veridan.com.au</div>
  </section>

</div>
</body>
</html>
```